Website re-design wedding music business

I need my wordpress wedding music website redesigned. I'm a wedding pianist and also provide duo/trio entertainment with other musicians and looking for an overhaul of my wordpress site.

Website: tomaslevett.com.au

Target Market(s)

brides; engaged couples

Industry/Entity Type

Wedding

Number of Pages Required

5+ page

Colors

Designer to choose colors to be used in the design.

Requirements
Must have
• I'm looking to overhaul my website which is looking rather tired after 4 years. It is functional but not inviting to visitors. Initially my website started out as a solo piano player providing music for wedding. It is gradually growing now where brides can book
• 1) Solo Piano
• 2) Duo (any combination of Piano / Cello / Vocalist / Violin)
• 3) Trio (any combination of Piano/ Cello /Vocalist / Violin)
• in future it may increase to 4 / 5 /6 piece bands so that needs to be taken into account for the future growth where I'll recruit other musicians.
• Some other functionality I'd like to see
• - Visitors want a calendar to know availability of musicians
• - Automatically providing enquiry price & discount (if applicable)
• - Automating the booking form process (manual) - There's a PDF form I send to the customer after we go back/forth on email on songs/price etc but if more of it could be automated online that would be great. If move to online it would be good to be able to override the set prices with a custom price and also providing a payment gateway
• More Flexibility on pricing - customer selects type of artists they want and it calculates a price based on who they have chosen whether it is a ceremony or canapes or reception (or combination of any). Extra transport fee is added if >50km out of Melbourne.
• How would you re-design this website. Imagine you are a bride/groom looking to book wedding music services. I would love to see some concepts .
• Please indicate any other fees required for your submission and level of support post this competition. I would like this to be an on-going relationship.
Nice to have
• I'd preferably like the website to be in wordpress as I've been familiar with it over time and can do basic updates in the back end. Happy for other suggestions if you can convince me I should move away from wordpress.

```html
<!DOCTYPE html>
<html lang="en">
<head>
<meta charset="utf-8">
<title>Tomas Levett – Wedding Pianist</title>
<link href="https://fonts.googleapis.com/css2?family=Montserrat:wght@400;500;600;700;800&family=Open+Sans:wght@600;700;800&display=swap" rel="stylesheet">
<style>
  :root {
    --backdrop: #2a2a2a;
    --ink: #1c1c1c;
    --black: #000;
    --white: #fff;
    --panel-dark: #2d2d2d;
    --orange: #f7994a;
    --grey-tile: #c4c4c4;
    --grey-light: #e4e4e4;
    --grey-text: #8a8a8a;
  }
  * { box-sizing: border-box; margin: 0; padding: 0; }
  html, body {
    width: 1200px; height: 1200px; overflow: hidden;
    background: var(--backdrop);
    font-family: "Montserrat", sans-serif;
    color: var(--ink);
  }
  .page {
    position: absolute; left: 287px; top: 70px;
    width: 625px; height: 1060px;
    background: var(--white); overflow: hidden;
  }

  /* Hero */
  .hero { position: absolute; left: 0; top: 0; width: 625px; height: 295px; }
  .hero-photo {
    position: absolute; inset: 0;
    background:
      radial-gradient(ellipse 220px 160px at 440px 200px, rgba(220,220,220,.55), transparent 70%),
      radial-gradient(ellipse 160px 200px at 250px 150px, rgba(60,60,60,.6), transparent 70%),
      linear-gradient(180deg, #3a3a3a 0%, #555 45%, #6b6b6b 75%, #4a4a4a 100%);
  }
  .hero-shade { position: absolute; inset: 0; background: rgba(0,0,0,.18); }
  .brand { position: absolute; left: 98px; top: 20px; display: flex; align-items: center; gap: 5px; }
  .brand-mark { width: 28px; height: 28px; border-radius: 50%; background: var(--white); }
  .brand-name { color: var(--white); font-weight: 600; font-size: 10.5px; letter-spacing: .2px; }
  .nav { position: absolute; left: 362px; top: 30px; display: flex; gap: 7px; font-size: 5px; color: var(--white); }
  .nav .active { font-weight: 700; }
  .nav-toggle { position: absolute; left: 514px; top: 30px; width: 13px; }
  .nav-toggle span { display: block; height: 1.2px; background: var(--white); margin-bottom: 2px; }
  .hero-title {
    position: absolute; left: 0; width: 625px; top: 124px; text-align: center;
    font-family: "Open Sans", sans-serif; font-weight: 800; color: var(--white);
    font-size: 40px; line-height: 1; letter-spacing: -.5px;
  }
  .hero-sub {
    position: absolute; left: 0; width: 625px; top: 167px; text-align: center;
    font-family: "Open Sans", sans-serif; font-weight: 700; color: var(--white); font-size: 19px; line-height: 1;
  }
  .hero-text {
    position: absolute; left: 0; width: 625px; top: 189px; text-align: center;
    font-size: 6.3px; line-height: 8.5px; color: var(--white);
  }
  .btn {
    position: absolute; left: 276px; top: 217px; width: 74px; height: 21px;
    background: var(--orange); color: var(--white); border-radius: 2px;
    font-family: "Open Sans", sans-serif; font-weight: 700; font-size: 8px;
    display: flex; align-items: center; justify-content: center;
  }

  /* Intro band */
  .intro { position: absolute; left: 0; top: 295px; width: 288px; height: 102px; background: var(--panel-dark); }
  .intro-block { position: absolute; background: rgba(255,255,255,.035); }
  .intro h3 { position: absolute; left: 78px; top: 25px; font-size: 7px; font-weight: 700; color: var(--white); }
  .intro p { position: absolute; left: 78px; top: 38px; width: 190px; font-size: 5px; line-height: 7.3px; color: var(--white); }
  .intro .link { position: absolute; left: 78px; top: 69px; font-size: 5.5px; font-weight: 700; color: var(--white); }
  .awards h3 { position: absolute; left: 318px; top: 317px; font-size: 7px; font-weight: 600; color: var(--ink); }
  .awards p { position: absolute; left: 318px; top: 330px; font-size: 5px; color: #555; }
  .badge { position: absolute; top: 342px; width: 34px; height: 34px; border-radius: 50%; }
  .awards-line { position: absolute; left: 288px; top: 395px; width: 337px; height: 2px; background: #ececec; }

  /* Music */
  .section-title { position: absolute; left: 0; width: 625px; text-align: center; font-weight: 700; font-size: 12.5px; color: var(--ink); }
  .tiles { position: absolute; left: 284px; top: 470px; display: grid; grid-template-columns: repeat(5, 35px); gap: 5px 7.5px; }
  .tile { width: 35px; height: 35px; background: var(--grey-tile); display: flex; align-items: center; justify-content: center; }

  .feature { position: absolute; left: 0; top: 566px; width: 625px; height: 152px; }
  .feature-photo {
    position: absolute; left: 0; top: 0; width: 274px; height: 152px;
    background: linear-gradient(160deg, #8c8c8c 0%, #6a6a6a 40%, #3e3e3e 70%, #a5a5a5 100%);
  }
  .testimonial { position: absolute; left: 274px; top: 0; width: 351px; height: 152px; background: var(--black); color: var(--white); }
  .testimonial h4 { position: absolute; left: 28px; top: 17px; font-size: 6.5px; font-weight: 700; }
  .testimonial p { position: absolute; left: 28px; top: 41px; width: 186px; font-size: 4.9px; line-height: 7.6px; }
  .testimonial .author { position: absolute; left: 28px; top: 120px; font-size: 5.5px; font-weight: 700; }
  .quote { position: absolute; font-family: "Open Sans", sans-serif; font-weight: 800; color: #3a3a3a; font-size: 60px; line-height: 1; }

  .player { position: absolute; left: 79px; top: 470px; width: 177px; height: 182px; border-radius: 3px; overflow: hidden; box-shadow: 0 2px 6px rgba(0,0,0,.25); }
  .player-art {
    height: 96px;
    background: radial-gradient(ellipse 70px 50px at 110px 40px, #cfcfcf, transparent 70%),
                linear-gradient(150deg, #1a1a1a 0%, #444 45%, #9a9a9a 70%, #2a2a2a 100%);
  }
  .player-track { height: 29px; background: var(--orange); display: flex; align-items: center; padding-left: 9px; gap: 6px; color: var(--white); }
  .player-thumb { width: 28px; height: 20px; background: var(--black); }
  .player-track b { display: block; font-size: 6.5px; font-weight: 600; }
  .player-track small { display: block; font-size: 4.8px; }
  .player-progress { height: 23px; background: #2b2b2b; position: relative; }
  .bar { position: absolute; left: 7px; right: 9px; top: 9px; height: 5px; border-radius: 3px; background: #dadada; }
  .bar-fill { position: absolute; left: 0; top: 0; width: 40px; height: 5px; border-radius: 3px; background: var(--orange); }
  .bar-knob { position: absolute; left: 35px; top: -2.5px; width: 10px; height: 10px; border-radius: 50%; background: var(--orange); border: 2px solid var(--white); }
  .player-controls { height: 34px; background: var(--grey-light); display: flex; align-items: center; justify-content: center; gap: 22px; }

  /* Events */
  .event { position: absolute; top: 786px; width: 110px; text-align: center; }
  .event-date {
    width: 75px; height: 75px; border-radius: 50%; background: var(--ink); margin: 0 auto;
    color: var(--white); display: flex; align-items: center; justify-content: center;
    font-weight: 700; font-size: 14px;
  }
  .event-date sup { font-size: 7.5px; vertical-align: 6px; }
  .event h5 { margin-top: 6px; font-size: 7px; font-weight: 700; line-height: 9.5px; color: var(--ink); }
  .event .venue { font-size: 4.8px; color: var(--grey-text); line-height: 8px; }
  .event .time { font-size: 7px; font-weight: 700; color: var(--orange); line-height: 10px; }
  .dots { position: absolute; left: 291px; top: 940px; display: flex; gap: 6px; }
  .dots span { width: 6px; height: 6px; border-radius: 50%; background: #bdbdbd; }
  .dots .on { background: var(--orange); }

  /* Footer */
  .footer { position: absolute; left: 0; top: 968px; width: 625px; height: 59px; background: var(--black); display: flex; align-items: center; justify-content: center; gap: 14px; }
  .social { display: flex; align-items: center; gap: 3px; color: var(--white); font-size: 7px; font-weight: 600; }
  .social i { width: 5px; height: 5px; border-radius: 50%; background: var(--white); display: block; }
  .copyright { position: absolute; left: 0; width: 625px; top: 1039px; text-align: center; font-size: 5px; color: #333; }
</style>
</head>
<body>
<main class="page">

  <header class="hero">
    <div class="hero-photo" role="img" aria-label="Black and white photo of the pianist at a white grand piano beneath large trees"></div>
    <div class="hero-shade"></div>
    <div class="brand"><span class="brand-mark"></span><span class="brand-name">TOMAS LEVETT</span></div>
    <nav class="nav">
      <span class="active">Home</span><span>About Tomas</span><span>Events</span><span>Music</span><span>Video</span><span>Contact</span>
    </nav>
    <div class="nav-toggle"><span></span><span></span><span></span></div>
    <h1 class="hero-title">TOMAS LEVETT</h1>
    <h2 class="hero-sub">Wedding Pianist | Event Pianist</h2>
    <p class="hero-text">Tomas Levett is a Melbourne professional pianist with over 5 years experience<br>within the wedding industry and has played piano for more than 30 years.</p>
    <a class="btn">Book Now</a>
  </header>

  <section class="intro">
    <div class="intro-block" style="left:25px;top:24px;width:60px;height:52px"></div>
    <div class="intro-block" style="left:45px;top:0;width:85px;height:35px"></div>
    <div class="intro-block" style="left:210px;top:0;width:60px;height:30px"></div>
    <div class="intro-block" style="left:120px;top:60px;width:80px;height:42px"></div>
    <h3>MELBOURNE PROFESSIONAL PIANIST</h3>
    <p>Tomas Levett is Melbourne's premier award wedding &amp; event pianist specialising in playing beautiful background music for weddings, special occasions &amp; corporate events.</p>
    <span class="link">Book Now</span>
  </section>

  <section class="awards">
    <h3>AWARDS &amp; ASSOCIATIONS</h3>
    <p>Best Victorian Supplier for Ceremony Music</p>
    <span class="badge" style="left:317px;background:#2f2f2f"></span>
    <span class="badge" style="left:364px;background:#d9a934"></span>
    <span class="badge" style="left:411px;background:#aab3c6"></span>
    <div class="awards-line"></div>
  </section>

  <h2 class="section-title" style="top:428px">TOMAS BEST MUSIC</h2>
  <div class="tiles">
    <div class="tile"><svg width="14" height="16" viewBox="0 0 14 16"><path d="M5 1h6v3H7v8.5a3 3 0 1 1-2-2.8z" fill="#fff"/></svg></div>
    <div class="tile"><svg width="14" height="16" viewBox="0 0 14 16"><path d="M5 1h6v3H7v8.5a3 3 0 1 1-2-2.8z" fill="#fff"/></svg></div>
    <div class="tile"><svg width="14" height="16" viewBox="0 0 14 16"><path d="M5 1h6v3H7v8.5a3 3 0 1 1-2-2.8z" fill="#fff"/></svg></div>
    <div class="tile"><svg width="14" height="16" viewBox="0 0 14 16"><path d="M5 1h6v3H7v8.5a3 3 0 1 1-2-2.8z" fill="#fff"/></svg></div>
    <div class="tile"><svg width="14" height="16" viewBox="0 0 14 16"><path d="M5 1h6v3H7v8.5a3 3 0 1 1-2-2.8z" fill="#fff"/></svg></div>
    <div class="tile"><svg width="14" height="16" viewBox="0 0 14 16"><path d="M5 1h6v3H7v8.5a3 3 0 1 1-2-2.8z" fill="#fff"/></svg></div>
    <div class="tile"><svg width="14" height="16" viewBox="0 0 14 16"><path d="M5 1h6v3H7v8.5a3 3 0 1 1-2-2.8z" fill="#fff"/></svg></div>
    <div class="tile"><svg width="14" height="16" viewBox="0 0 14 16"><path d="M5 1h6v3H7v8.5a3 3 0 1 1-2-2.8z" fill="#fff"/></svg></div>
    <div class="tile"><svg width="14" height="16" viewBox="0 0 14 16"><path d="M5 1h6v3H7v8.5a3 3 0 1 1-2-2.8z" fill="#fff"/></svg></div>
    <div class="tile"><svg width="14" height="16" viewBox="0 0 14 16"><path d="M5 1h6v3H7v8.5a3 3 0 1 1-2-2.8z" fill="#fff"/></svg></div>
  </div>

  <section class="feature">
    <div class="feature-photo" role="img" aria-label="Photo of the pianist seated on a piano bench outdoors"></div>
    <div class="testimonial">
      <span class="quote" style="left:10px;top:2px">&ldquo;</span>
      <h4>TESTIMONIALS</h4>
      <p>Tom did a great job entertaining our guests in-between our ceremony and reception while we had photos taken. He has a large variety of music he can play and is very willing to learn new songs if you have any special requests. Would definitely recommend him for other weddings and events.</p>
      <span class="quote" style="left:188px;top:78px">&rdquo;</span>
      <span class="author">Clara &amp; James</span>
    </div>
  </section>

  <div class="player">
    <div class="player-art" role="img" aria-label="Close-up photo of piano keys"></div>
    <div class="player-track">
      <span class="player-thumb"></span>
      <span><b>HARBOURLIGHTS · HERE COMES</b><small>Musique douce et fréquences apaisantes</small></span>
    </div>
    <div class="player-progress"><div class="bar"><div class="bar-fill"></div><div class="bar-knob"></div></div></div>
    <div class="player-controls">
      <svg width="12" height="10" viewBox="0 0 12 10"><rect x="0" y="0" width="2" height="10" fill="#555"/><path d="M11 0v10L3 5z" fill="#555"/></svg>
      <svg width="22" height="22" viewBox="0 0 22 22"><rect x="1" y="1" width="20" height="20" fill="none" stroke="#f7994a" stroke-width="1.6"/><path d="M8 6v10l8-5z" fill="none" stroke="#f7994a" stroke-width="1.4"/></svg>
      <svg width="12" height="10" viewBox="0 0 12 10"><path d="M1 0v10l8-5z" fill="#555"/><rect x="10" y="0" width="2" height="10" fill="#555"/></svg>
    </div>
  </div>

  <h2 class="section-title" style="top:740px">UPCOMING EVENTS</h2>
  <article class="event" style="left:87px"><div class="event-date">17<sup>AUG</sup></div><h5>WEDDING<br>CEREMONY &amp; CANAPES</h5><div class="venue">WILLOWBANK ESTATE YARRA VALLEY</div><div class="time">3:30 PM - 6:00 PM</div></article>
  <article class="event" style="left:201px"><div class="event-date">17<sup>AUG</sup></div><h5>WEDDING<br>CEREMONY &amp; CANAPES</h5><div class="venue">WILLOWBANK ESTATE YARRA VALLEY</div><div class="time">3:30 PM - 6:00 PM</div></article>
  <article class="event" style="left:314px"><div class="event-date">17<sup>AUG</sup></div><h5>WEDDING<br>CEREMONY &amp; CANAPES</h5><div class="venue">WILLOWBANK ESTATE YARRA VALLEY</div><div class="time">3:30 PM - 6:00 PM</div></article>
  <article class="event" style="left:427px"><div class="event-date">17<sup>AUG</sup></div><h5>WEDDING<br>CEREMONY &amp; CANAPES</h5><div class="venue">WILLOWBANK ESTATE YARRA VALLEY</div><div class="time">3:30 PM - 6:00 PM</div></article>
  <div class="dots"><span></span><span></span><span class="on"></span></div>

  <footer class="footer">
    <span class="social"><i></i>Friends</span>
    <span class="social"><i></i>Updates</span>
    <span class="social"><i></i>Circles</span>
    <span class="social"><i></i>Videos</span>
  </footer>
  <p class="copyright">© 2017 Copyright Tomas Levett I All Right Reserved</p>

</main>
</body>
</html>
```